“Bright Tide” Spring Fair Poster

We are putting together a school and community fair. We need a poster designed to advertise the event and give some important information to would be attendees. We’d like the poster graphics to evoke a minimalistic and futuristic aesthetic, be bold, yet fun! We will printing the posters, so we will need for them to be at high resolution and ready to send to print.

Target Market(s)

Students, Parents, and Community members

Industry/Entity Type

School

Font styles to use
Sans Serif

Colors
33a6d7
fabb78
9d9d9d
ffffff
1b1b1b
33b8a4

Requirements
Must have
• Bright Tide
• Birch & Lantern Spring Fair 2018
• Friday, May 18th
• 5:00-9:00pm
• Tickets Will Be Available at Select Pick up & Drop Off Times
• Come Enjoy a Futuristic Evening of Food, Music, Entertainment, & Fun!
Nice to have
• We’d love to see a bold and graphic poster with a futuristic feel!
• See the sample image below from previous event poster and additional images for mood and inspiration. Would love to see metallics (silver or metallic colors)

```html
<!DOCTYPE html>
<html lang="en">
<head>
<meta charset="utf-8">
<title>Bright Tide – Birch &amp; Lantern Spring Fair 2018</title>
<link href="https://fonts.googleapis.com/css2?family=Bungee+Inline&family=Montserrat:wght@600;700;800&display=swap" rel="stylesheet">
<style>
  :root {
    --sky-blue: #4a78b0;
    --sky-deep: #2f5a93;
    --cloud-grey: #8f949c;
    --ink: #1b1b1b;
    --gold-light: #f8d77a;
    --gold-mid: #e0a24a;
    --gold-deep: #a8621e;
    --band: rgba(236, 236, 238, 0.82);
    --hero-blue: #4d6fa3;
    --hero-warm: #b8633a;
  }
  html, body {
    margin: 0;
    width: 960px;
    height: 1200px;
    overflow: hidden;
    background: #6b6b6b;
  }
  .poster {
    position: relative;
    width: 960px;
    height: 1200px;
    overflow: hidden;
    font-family: "Montserrat", Arial, sans-serif;
    text-align: center;
  }
  .sky-backdrop {
    position: absolute;
    inset: 0;
    background: linear-gradient(180deg, var(--sky-deep) 0%, var(--sky-blue) 45%, var(--cloud-grey) 78%, #6f747c 100%);
  }
  .hero-art {
    position: absolute;
    left: 0;
    top: 0;
    width: 960px;
    height: 610px;
  }
  .gold-text {
    background: linear-gradient(180deg, var(--gold-light) 0%, var(--gold-mid) 55%, var(--gold-deep) 100%);
    -webkit-background-clip: text;
    background-clip: text;
    color: transparent;
  }
  .title {
    position: absolute;
    left: 0;
    right: 0;
    top: 620px;
    margin: 0;
    font-family: "Bungee Inline", "Arial Black", sans-serif;
    font-weight: 400;
    font-size: 94px;
    line-height: 1;
    letter-spacing: 1px;
    filter: drop-shadow(2px 2px 0 rgba(0,0,0,0.55));
  }
  .subtitle {
    position: absolute;
    left: 0;
    right: 0;
    top: 716px;
    margin: 0;
    font-weight: 800;
    font-size: 47px;
    line-height: 1.1;
    filter: drop-shadow(2px 2px 0 rgba(0,0,0,0.5));
  }
  .details {
    color: var(--ink);
    font-weight: 700;
  }
  .details p {
    position: absolute;
    left: 0;
    right: 0;
    margin: 0;
    line-height: 1;
    font-size: 36px;
  }
  .details .date { top: 816px; }
  .details .time { top: 870px; }
  .details .tickets-1 { top: 930px; }
  .details .tickets-2 { top: 974px; }
  .invite-band {
    position: absolute;
    left: 0;
    right: 0;
    top: 1043px;
    height: 136px;
    background: var(--band);
    display: flex;
    align-items: center;
    justify-content: center;
  }
  .invite {
    margin: 0;
    font-weight: 800;
    font-size: 42px;
    line-height: 48px;
    filter: drop-shadow(1px 1px 0 rgba(0,0,0,0.35));
  }
</style>
</head>
<body>
<main class="poster">
  <div class="sky-backdrop" role="img" aria-label="Soft cloudy blue and grey sky background"></div>

  <svg class="hero-art" viewBox="0 0 960 610" role="img" aria-label="Cosmic illustration: two hands holding a glowing energy orb with lightning above clouds, framed by peeled-back page corners">
    <defs>
      <linearGradient id="hero-fill" x1="0" y1="0" x2="1" y2="0">
        <stop offset="0%" stop-color="var(--hero-blue)"/>
        <stop offset="50%" stop-color="var(--hero-warm)"/>
        <stop offset="100%" stop-color="var(--hero-blue)"/>
      </linearGradient>
    </defs>
    <path d="M0 0 H960 V440 Q480 790 0 440 Z" fill="url(#hero-fill)"/>
  </svg>

  <h1 class="title gold-text">BRIGHT TIDE</h1>
  <h2 class="subtitle gold-text">Birch &amp; Lantern Spring Fair 2018</h2>

  <section class="details">
    <p class="date">Friday, May 18th</p>
    <p class="time">5:00-9:00pm</p>
    <p class="tickets-1">Tickets Will Be Available at</p>
    <p class="tickets-2">Select Pick up &amp; Drop Off Times</p>
  </section>

  <div class="invite-band">
    <p class="invite gold-text">Come Enjoy a Futuristic Evening of<br>Food, Music, Entertainment, &amp; Fun!</p>
  </div>
</main>
</body>
</html>
```